Building Referrer Relationships Booklet

4 page A4 booklet to give to potential professional referrers to establish a collaborative relationship.Needs to be bright, vibrant, colourful, friendly, inviting, in keeping with The Stride Studio colours.
Want to provide potential referrer partners a great reason to choose to collaborate with us. They need to know who we are, what makes us different/appealing, and who we are looking for to connect with.
The final product should communicate high performance and connectedness.

Target Market(s)

professional medical allied health and fitness practitioners

Industry/Entity Type

Health

Requirements
Must have
• energetic, vibrant, engaging, inviting, images

```html
<!DOCTYPE html>
<html lang="en">
<head>
<meta charset="utf-8">
<title>Referral Partnerships Booklet – The Stride Studio</title>
<link href="https://fonts.googleapis.com/css2?family=Fira+Sans:wght@400;500;600;700&family=Montserrat:wght@500;600;700&family=Open+Sans:wght@400;600;700&display=swap" rel="stylesheet">
<style>
:root{
  --backdrop:#555555;
  --paper:#ffffff;
  --navy:#14345f;
  --navy-deep:#0f2d6b;
  --sky:#29a8e0;
  --band:#b2e6fb;
  --ink:#2b2b2b;
  --red:#ee3b3b;
  --green:#0d5a2b;
  --rust:#a0522d;
  --royal:#1d4fa3;
}
*{margin:0;padding:0;box-sizing:border-box}
html,body{width:1200px;height:1200px;overflow:hidden;background:var(--backdrop)}
body{position:relative;font-family:"Open Sans",sans-serif;color:var(--ink)}
.page{position:absolute;width:387px;height:549px;background:var(--paper);overflow:hidden}
.page--cover{left:175px;top:39px}
.page--about{left:638px;top:39px}
.page--way{left:175px;top:612px}
.page--partners{left:638px;top:612px}
.abs{position:absolute}

/* cover */
.cover-block{background:var(--navy);left:0;width:86px}
.cover-block--top{top:0;height:152px}
.cover-block--bottom{top:486px;height:63px}
.cover-title{left:105px;top:30px;font-family:"Fira Sans",sans-serif;font-weight:700;font-size:31px;line-height:31px;color:var(--navy);letter-spacing:.5px}
.cover-sub{left:105px;top:62px;font-family:"Fira Sans",sans-serif;font-weight:500;font-size:22px;line-height:22px;color:var(--sky);letter-spacing:.6px}
.cover-tag{left:105px;top:90px;font-family:"Fira Sans",sans-serif;font-size:14px;color:var(--ink)}
.cover-help{left:106px;top:133px;font-family:"Fira Sans",sans-serif;font-size:11px;color:var(--ink)}
.cover-photo{left:0;top:154px;width:387px;height:329px;background:linear-gradient(140deg,#3a2a22 0%,#c79a6e 35%,#d8b48c 55%,#7a6a60 80%,#e8e4df 100%)}
.cover-close{left:106px;top:495px;font-family:"Fira Sans",sans-serif;font-size:14px;line-height:19px;color:var(--ink)}

/* about */
.h-label{font-family:"Montserrat",sans-serif;font-weight:700;color:var(--navy)}
.about-title{left:19px;top:15px;font-size:10.5px}
.value-tabs{left:19px;top:38px;display:flex;gap:2px}
.value-tab{width:56.5px;height:12px;font-family:"Montserrat",sans-serif;font-weight:700;font-size:6px;color:#fff;display:flex;align-items:center;justify-content:center;letter-spacing:.3px}
.value-list{left:19px;top:58px;width:352px;font-size:6.2px;line-height:8px}
.value-list p{margin-bottom:11.5px}
.value-list b{font-weight:700}
.about-lead{left:19px;top:208px;width:355px;font-family:"Montserrat",sans-serif;font-weight:500;font-size:10px;line-height:12.5px;color:var(--navy-deep)}
.about-band{left:0;top:250px;width:387px;height:168px;background:var(--band)}
.love-head{left:19px;top:13px;font-family:"Montserrat",sans-serif;font-weight:600;font-size:8px;line-height:11px;color:var(--navy-deep)}
.love-list{left:19px;top:50px;width:250px;list-style:none;font-family:"Montserrat",sans-serif;font-size:7px;line-height:9px;color:var(--navy-deep)}
.love-list li{margin-bottom:17px;padding-left:12px;position:relative}
.love-list li span{position:absolute;left:0;font-weight:600}
.love-list strong{font-weight:600}
.love-list em{font-style:normal;font-weight:500;color:#29537f}
.foot-photo{left:278px;top:11px;width:90px;height:148px;border:2px solid #fff;background:linear-gradient(180deg,#1a1a1a,#8a8a8a 45%,#3a3a3a 80%,#111)}

.info-box{border:1px solid var(--navy);border-radius:2px}
.info-box__legend{position:absolute;top:-6px;left:7px;background:var(--paper);padding:0 3px;font-family:"Montserrat",sans-serif;font-weight:600;font-size:8.5px;color:var(--navy-deep)}
.dot-list{position:absolute;list-style:none;font-family:"Montserrat",sans-serif;font-weight:500;font-size:6px;line-height:7px;color:var(--ink)}
.dot-list li{position:relative;padding-left:9px}
.dot-list li::before{content:"";position:absolute;left:0;top:1px;width:4px;height:4px;border-radius:50%;border:1.2px solid var(--sky)}
.team-box{left:18px;top:452px;width:351px;height:63px}

/* way */
.way-title{left:18px;top:15px;font-family:"Montserrat",sans-serif;font-weight:600;font-size:12px;letter-spacing:.8px;color:var(--navy)}
.way-intro{left:18px;top:34px;width:351px;font-size:7.4px;line-height:9.2px;text-align:justify;color:#444}
.way-band{left:0;top:83px;width:387px;height:348px;background:var(--band)}
.step-col{position:absolute;font-size:6.6px;line-height:9.4px;color:#222}
.step-col h3{font-family:"Montserrat",sans-serif;font-weight:600;font-size:7px;letter-spacing:.4px;margin-bottom:4px}
.step-col .step{margin-bottom:5px}
.step-col .step b{font-weight:700}
.step-col .step div{padding-left:8px}
.collage{left:198px;top:83px;width:171px;height:258px;border:2px solid #fff;background:#fff;display:grid;grid-template-columns:1fr 1fr;grid-template-rows:93px 78px 1fr;gap:2px}
.collage__tile{background:linear-gradient(160deg,#b58e6a,#6e5c4f 55%,#c9bfb4)}
.collage__tile--wide{grid-column:1 / 3;background:linear-gradient(170deg,#9a8c80,#4e4a48 50%,#c0654a 90%)}
.collage__tile--tall{grid-row:2 / 4;grid-column:2;background:linear-gradient(180deg,#e8e6e2,#b89878 60%,#8a5e3c)}
.achieve-box{left:18px;top:446px;width:351px;height:82px}
.achieve-list--left{left:12px;top:16px;width:172px}
.achieve-list--right{left:194px;top:16px;width:150px}

/* partners */
.athlete-box{left:18px;top:26px;width:351px;height:75px}
.partners-band{left:0;top:115px;width:387px;height:343px;background:var(--band)}
.partners-head{left:18px;top:14px;font-family:"Montserrat",sans-serif;font-weight:600;font-size:7.4px;letter-spacing:.5px;color:var(--navy-deep)}
.partner-list{position:absolute;left:18px;top:37px;width:350px;list-style:none;font-size:6.5px;line-height:9.2px;color:#222}
.partner-list li{margin-bottom:8.4px}
.partner-list b{font-weight:600;color:#0f2d6b}
.partner-list b::before{content:"• "}
.partner-list div{padding-left:12px}
.badge-row{left:18px;top:484px;width:352px;height:36px;display:flex;justify-content:space-between;align-items:center}
.badge{background:#d7dde4}
.badge--circle{width:36px;height:36px;border-radius:50%;background:#d94040}
.badge--sq{width:44px;height:28px;background:var(--royal)}
.badge--wide{width:60px;height:22px;background:#f2a03a}
.badge--mid{width:64px;height:18px;background:#9a9a9a}
.badge--red{width:58px;height:20px;background:var(--red)}
.badge--tall{width:24px;height:36px;background:#f47a20}
</style>
</head>
<body>

<!-- Page 1 · Cover -->
<section class="page page--cover">
  <div class="abs cover-block cover-block--top"></div>
  <h1 class="abs cover-title">REFERRAL</h1>
  <div class="abs cover-sub">PARTNERSHIPS</div>
  <div class="abs cover-tag">Because Together We Achieve More</div>
  <div class="abs cover-help">We are here to help our clients get back on their feet.</div>
  <div class="abs cover-photo" role="img" aria-label="Photo of many hands stacked together in a team huddle over a wooden floor"></div>
  <div class="abs cover-block cover-block--bottom"></div>
  <div class="abs cover-close">Let’s combine our skillsets<br>so we can achieve even better results.</div>
</section>

<!-- Page 2 · About us -->
<section class="page page--about">
  <h2 class="abs h-label about-title">ABOUT US:</h2>
  <div class="abs value-tabs">
    <span class="value-tab" style="background:var(--sky)">COURAGE</span>
    <span class="value-tab" style="background:var(--red)">INSPIRATION</span>
    <span class="value-tab" style="background:var(--navy-deep)">FUN</span>
    <span class="value-tab" style="background:var(--green)">CREATIVE</span>
    <span class="value-tab" style="background:var(--rust)">WOW</span>
    <span class="value-tab" style="background:var(--royal)">TEAM</span>
  </div>
  <div class="abs value-list">
    <p><b style="color:var(--sky)">Courage</b> gives us the strength and confidence to take risks and embrace challenges</p>
    <p><b style="color:var(--red)">Inspiration</b> is our energy, our fuel for success, that life force that feeds us as we grow and develop.</p>
    <p><b style="color:var(--navy-deep)">Fun</b> generates happiness, and we all function at our best when we are happy.</p>
    <p><b style="color:var(--green)">Creativity</b> sets us as an innovative leading-edge business.</p>
    <p><b style="color:var(--rust)">Wow</b> means being the very best we can be and realise our true potential.We are not your average business, our service is not average, and our people are not average.</p>
    <p><b style="color:var(--royal)">Team</b> and in particular high-performanceteam means we perform at our very best. Great teamwork creates unity and we accomplish much more than each of us alone.</p>
  </div>
  <p class="abs about-lead">AtThe Stride Studio, we are passionate about building strong postural foundations, from the feet up.</p>
  <div class="abs about-band">
    <div class="abs love-head">The top 3 things our clients love about us<br>(and hopefully yours will too!):</div>
    <ol class="abs love-list">
      <li><span>1.</span><strong>Positive energy, enthusiasm and outcomes</strong><br><em>NPS average score &gt;9 out of 10</em></li>
      <li><span>2.</span><strong>Trusted leader in the practice of podiatric medicine</strong><br><em>established 1999, elite experience, latest high-tech equipment</em></li>
      <li><span>3.</span><strong>Focus is on strong feet, not just orthotics!</strong><br><em>StrongBase Barefoot Technology, Fascial Lines, Hands-On Foot Therapy</em></li>
    </ol>
    <div class="abs foot-photo" role="img" aria-label="Black and white close-up photo of the sole of a strong foot"></div>
  </div>
  <div class="abs info-box team-box">
    <span class="info-box__legend">Our Team:</span>
    <ul class="dot-list" style="left:10px;top:15px">
      <li style="margin-bottom:9px">Dr Marcus Feldane (Principal Podiatrist)</li>
      <li style="margin-bottom:9px">Dr Clara Whitby (Senior Podiatrist)</li>
      <li>Dr Nina Castell (Podiatrist)</li>
    </ul>
    <ul class="dot-list" style="left:188px;top:15px">
      <li style="margin-bottom:9px">Dr Tobias Lenn (Podiatrist)</li>
      <li style="margin-bottom:9px">Jodie Parnell (Practice Manager)</li>
      <li>Leah Margrave (Front Office Administrator)</li>
    </ul>
  </div>
</section>

<!-- Page 3 · The way -->
<section class="page page--way">
  <h2 class="abs way-title">THE STRIDE STUDIO WAY</h2>
  <p class="abs way-intro">Our pathway to strengthen postural foundations, to create lasting changes for freedom of movement, and ultimately keep us going well beyond what we thought was possible (updated as research and tech changes).</p>
  <div class="abs way-band">
    <div class="step-col" style="left:18px;top:8px;width:178px">
      <h3>FIX YOUR FEET</h3>
      <div class="step"><b>1. Fix</b>the pain<div>Provide analgesia<br>Reduce inflammation<br>Corn/callus/foreign body removal<br>Ingrown/thickened toenail repair and maintenance Surgery</div></div>
      <div class="step"><b>3. Strengthen</b> the feet<div>(increase strength and resilience)<br>Strengthen intrinsics<br>Connect foot strength to core strength<br>Stimulate neuromuscular strength</div></div>
      <h3 style="margin-top:13px">BIOHACK YOUR BODY</h3>
      <div class="step"><b>4. Protect</b> the whole body (stability)<div>Optimise Postural Alignment<br>Activate neuromuscular/reflexive balance stability<br>Customised corrective exercises<br>Improve cellular regeneration<br>Optimise nutrition/healthy gut<br>Optimise healthy mind</div></div>
      <div class="step" style="margin-top:11px"><b>5. Strengthen</b> the whole body (strength, elasticity)<div>Strengthen the deep core (stabilisers)<br>Strengthen the outer core (mobilisers)<br>Increase fascial elasticity/strength<br>Increase functional strength<br>Increase endurance<br>Customised nutrition for specific performance<br>Improve psychological resilience</div></div>
      <div class="step" style="margin-top:8px"><b>6. Repeat</b> consistently</div>
    </div>
    <div class="step-col" style="left:198px;top:20px;width:180px">
      <div class="step"><b>2. Protect</b> the feet (reduce damage,<div>optimise stability, promote healing)<br>Reduce tissue damage<br>Optimise Foot Posture<br>Activate neuromuscular/reflexive balance stability<br>Promote tissue repair/cellular regeneration</div></div>
    </div>
    <div class="abs collage">
      <div class="collage__tile collage__tile--wide" role="img" aria-label="Group photo of workshop participants standing and kneeling together"></div>
      <div class="collage__tile" role="img" aria-label="Photo of a presenter teaching a small seated group"></div>
      <div class="collage__tile collage__tile--tall" role="img" aria-label="Photo of a large class doing barefoot exercises in a training room"></div>
      <div class="collage__tile" role="img" aria-label="Photo of two clinicians presenting side by side"></div>
    </div>
  </div>
  <div class="abs info-box achieve-box">
    <span class="info-box__legend">Our Team Achievements:</span>
    <ul class="dot-list achieve-list--left">
      <li style="margin-bottom:9px">Director, Sports Medicine Alliance (SMAL)</li>
      <li style="margin-bottom:10px">Director, Regional Academy of Podiatric<br>Sports Medicine (RAPSM).</li>
      <li style="margin-bottom:9px">External Advisor, Westvale Podiatric Unit</li>
      <li>StrongBase Level 1 Barefoot Rehabilitation Instructor</li>
    </ul>
    <ul class="dot-list achieve-list--right">
      <li style="margin-bottom:9px">Hands-On Foot Therapy trained</li>
      <li style="margin-bottom:9px">Fascial Lines trained</li>
      <li>Class 3b Laser Certified</li>
    </ul>
  </div>
</section>

<!-- Page 4 · Partners -->
<section class="page page--partners">
  <div class="abs info-box athlete-box">
    <span class="info-box__legend">Our Elite Athlete Experience:</span>
    <ul class="dot-list" style="left:10px;top:15px">
      <li style="margin-bottom:12.5px">National Sports Academy (NSA)</li>
      <li style="margin-bottom:12.5px">Coastal Rugby Squad</li>
      <li>Harbour City Games</li>
    </ul>
    <ul class="dot-list" style="left:188px;top:15px">
      <li style="margin-bottom:12.5px">Westshore Triathlon Championships</li>
      <li style="margin-bottom:12.5px">Southbay Regional Games</li>
      <li>Westshore Tennis Cup</li>
    </ul>
  </div>
  <div class="abs partners-band">
    <h2 class="abs partners-head">REFERRAL PARTNERS REQUIRED:</h2>
    <ul class="partner-list">
      <li><b>Massage therapists</b><div>Deep tissue and remedial massage<br>Therapeutic massage</div></li>
      <li><b>Fascial therapists</b><div>Fascial Lines fascial releases to reset the alignment of the whole body</div></li>
      <li><b>Physiotherapists</b><div>Pain relief, protect and strengthen both lower limb and upper limb</div></li>
      <li><b>GP, Sports Physicians</b><div>General health,diagnostics, treatment support, prescription medications<br>Specialist referrals</div></li>
      <li><b>Osteopaths and chiropractors</b><div>Mobilisation and manipulative therapy for the spinal column and limbs</div></li>
      <li><b>Dietician and nutritionists</b><div>DEXA scan for bone density/lean mass/fat mass<br>Optimising gut health and nutrition - You are what you eat!</div></li>
      <li><b>Psychologists/psychiatrists</b><div>Sometimes ourphysical body cannot get better until we optimise a healthy mind</div></li>
      <li><b>Personal trainers, Pilates and yoga instructors</b><div>Create awesome body strength, flexibility and resilience</div></li>
      <li><b>Surgeons</b><div>When conservative methods are ineffective, surgical intervention works well.</div></li>
    </ul>
  </div>
  <div class="abs badge-row" aria-label="Partner badges">
    <span class="badge badge--circle"></span>
    <span class="badge badge--sq"></span>
    <span class="badge badge--wide"></span>
    <span class="badge badge--mid"></span>
    <span class="badge badge--red"></span>
    <span class="badge badge--tall"></span>
  </div>
</section>

</body>
</html>
```